Brightfield Training Course Outline re-design

We are wanting to re-design our template for course outlines. Course outlines are provided to prospective students wanting to find out more information about a course. Our website was recently revamped so we would want the new course outlines to have a similar look and feel to our website: www.brightfieldtraining.com.au
I have attached a current course outline. All content from the current outline must come across to the new one. We want to appeal to adult students wanting to work with children. We emphasise flexible timeframes, easy-to-use online system, prompt and friendly support from a trainer. We want to inspire people to engage in education and change their lives. This is reflected in our motto - Study | Brightfield | Achieve.
Ideally, this will become a template for other course outlines, so if the file can be provided in PDF as well as an editable format it would be greatly appreciated.
The colour codes from our website are:
Aqua: #81c9bd
Grey: #939598
Blue: #000080
Looking forward to responses.
Happy to email any images or logos needed.

Target Market(s)

Mums with children wanting to re-enter the workforce

Requirements
Must have
• All content from current course outline must come across.
• Brightfield Training logo

```html
<!DOCTYPE html>
<html lang="en">
<head>
<meta charset="utf-8">
<title>Brightfield Training – Course Outline CHC30213</title>
<link rel="stylesheet" href="https://fonts.googleapis.com/css2?family=Lato:wght@400;700;900&display=swap">
<style>
:root{
  --navy:#000080;
  --navy-deep:#07077a;
  --aqua:#81c9bd;
  --grey:#939598;
  --stage:#5a5a5c;
  --heading:#1c1cae;
  --ink:#2b2b33;
  --white:#ffffff;
}
*{box-sizing:border-box;margin:0;padding:0}
html,body{width:1200px;height:1200px;overflow:hidden}
body{background:var(--stage);font-family:"Lato",Arial,sans-serif;color:var(--ink);position:relative}

.page{position:absolute;background:var(--white);overflow:hidden;box-shadow:0 2px 8px rgba(0,0,0,.45)}
.page--cover{left:97px;top:58px;width:386px;height:542px;background:var(--navy)}
.page--units{left:699px;top:59px;width:384px;height:539px}
.page--study{left:97px;top:625px;width:381px;height:535px}
.page--fees{left:702px;top:625px;width:384px;height:540px}

/* cover */
.cover__photo{position:absolute;left:0;top:0;width:386px;height:400px;
  background:linear-gradient(160deg,#c9d3dc 0%,#8fa6bf 35%,#5d7fa8 60%,#b9c2c9 100%)}
.cover__shapes{position:absolute;left:0;top:0;width:386px;height:542px}
.cover__brand{position:absolute;left:16px;top:22px;display:flex;align-items:center;gap:6px;
  font-weight:900;font-size:22px;color:var(--navy);letter-spacing:-.3px}
.cover__brand-dot{width:12px;height:12px;border-radius:50%;background:var(--navy)}
.cover__title{position:absolute;left:0;width:100%;top:392px;text-align:center;color:var(--white);
  font-weight:900;font-size:30px;letter-spacing:.3px}
.cover__subtitle{position:absolute;left:0;width:100%;top:432px;text-align:center;color:var(--white);
  font-size:15.5px;font-weight:400}
.cover__intro{position:absolute;left:14px;right:14px;top:460px;color:var(--white);font-size:6.4px;
  line-height:1.3;text-align:justify}
.cover__band{position:absolute;left:0;bottom:0;width:100%;height:36px;background:var(--aqua);
  display:flex;align-items:center;justify-content:center;gap:5px;font-size:8.5px;font-weight:700;
  color:var(--ink);letter-spacing:.8px}
.globe{width:9px;height:9px}

/* shared inner pages */
.sidebar{position:absolute;left:0;top:0;bottom:0;background:var(--navy)}
.page--units .sidebar{width:99px}
.page--study .sidebar{width:106px}
.page--fees .sidebar{width:102px}
.motto{position:absolute;left:10px;right:8px;top:10px;display:flex;flex-direction:column;gap:14px}
.motto__pill{height:22px;border-radius:11px;background:var(--aqua);color:var(--navy);
  font-weight:700;font-size:11px;letter-spacing:.4px;display:flex;align-items:center;justify-content:center}
.sidebar__photo{position:absolute;left:12px;right:2px;top:121px;height:210px}
.photo--class{background:linear-gradient(180deg,#b7c2cf 0%,#6f86a6 45%,#3b5479 80%,#9aa7b3 100%)}
.photo--student{background:linear-gradient(180deg,#e7dcc2 0%,#cdb98f 40%,#f1e7b9 70%,#c2b9a6 100%)}
.photo--learner{background:linear-gradient(180deg,#8ea4bd 0%,#5b6f8a 40%,#c9d5de 75%,#7f98b2 100%)}
.options{position:absolute;left:12px;top:350px;color:var(--white)}
.options__title{font-size:12px;font-weight:700;text-decoration:underline;margin:0 0 10px 4px}
.options__item{display:flex;align-items:center;gap:7px;font-size:9.5px;height:24px}
.options__item::before{content:"";width:8px;height:8px;border-radius:50%;background:var(--white)}
.footer{position:absolute;left:0;bottom:0;width:100%;height:78px}
.footer svg{position:absolute;inset:0;width:100%;height:100%}
.footer__url{position:absolute;left:12px;bottom:20px;font-size:8px;color:var(--white)}

.content{position:absolute;top:6px;bottom:70px;overflow:hidden}
.page--units .content{left:112px;right:9px;bottom:42px;z-index:2}
.page--study .content{left:113px;right:10px}
.page--fees .content{left:110px;right:10px}
.h{color:var(--heading);font-weight:900;font-size:8.6px;margin:3px 0 1px;letter-spacing:.1px}
.h small{font-weight:400;font-size:6.4px;color:var(--ink)}
.p{font-size:5.1px;line-height:1.28;text-align:justify;margin-bottom:2px}
.p b{font-weight:700}
.p u{text-decoration:underline}

.units{display:grid;grid-template-columns:47px 1fr;column-gap:6px;margin:5px 0 3px}
.units dt,.units dd{font-size:5.1px;line-height:1.2;min-height:12.6px;padding-top:1px}
.units dt{font-weight:700;text-align:right;padding-right:5px;border-right:.6px solid var(--ink)}
.units--elective dt,.units--elective dd{min-height:11px}
.note-band{margin:3px -9px 3px -10px;background:var(--aqua);padding:3px 10px;font-size:5px;font-weight:700;line-height:1.3}
.supplement{text-align:center;font-size:6.4px;margin-top:3px}
.supplement b{font-weight:700}
.supplement-rates{display:flex;justify-content:center;gap:10px;font-size:5px;font-weight:700;color:var(--heading);margin-top:5px}

.list{list-style:none;font-size:5.1px;line-height:1.28;margin:0 0 2px 4px}
.list li::before{content:"• ";font-weight:700}
.list--ticks li::before{content:"✓ "}
.list--num{list-style:decimal;margin-left:14px}
.list--num li::before{content:none}
.sub{display:flex;gap:4px;margin:2px 0 2px 18px}
.sub__mark{width:5px;height:5px;background:var(--heading);margin-top:1px;flex:none}
.tag{display:inline-block;background:var(--aqua);border-radius:5px;padding:0 5px;font-size:5.2px;font-weight:700;margin:2px 0}

.fees{width:240px;margin:3px 0 3px 10px;border-collapse:collapse;font-size:5.2px;background:var(--aqua)}
.fees th{background:var(--navy);color:var(--white);font-weight:400;text-align:left;padding:1px 4px}
.fees td{padding:2px 4px;vertical-align:top}
.fees td:last-child{width:50px}
.fees tr.row--split td{border-top:.6px solid var(--white)}
</style>
</head>
<body>

<!-- Cover -->
<section class="page page--cover">
  <div class="cover__photo" role="img" aria-label="Photo of adult students working together around a classroom table with a laptop"></div>
  <svg class="cover__shapes" viewBox="0 0 386 542" preserveAspectRatio="none" aria-hidden="true">
    <path d="M0,212 C40,320 180,400 386,372 L386,542 L0,542 Z" fill="#ffffff"/>
    <path d="M0,232 C50,338 190,410 386,384 L386,542 L0,542 Z" fill="#81c9bd"/>
    <path d="M0,250 C60,350 200,420 386,392 L386,542 L0,542 Z" fill="#000080"/>
  </svg>
  <div class="cover__brand"><span class="cover__brand-dot"></span>Brightfield Training</div>
  <h1 class="cover__title">COURSE OUTLINE</h1>
  <p class="cover__subtitle">CHC30213 Certificate III in Education Support</p>
  <p class="cover__intro">Welcome to Brightfield Training (RTO# 40718)! Thank you for considering us in the very important task of gaining a nationally recognised qualification. Please read this course outline and the student handbook prior to enrolling, these documents contain information crucial for successful study in this course.</p>
  <div class="cover__band">
    <svg class="globe" viewBox="0 0 10 10" aria-hidden="true"><circle cx="5" cy="5" r="4.3" fill="none" stroke="#2b2b33" stroke-width=".9"/><ellipse cx="5" cy="5" rx="1.9" ry="4.3" fill="none" stroke="#2b2b33" stroke-width=".8"/><line x1=".7" y1="5" x2="9.3" y2="5" stroke="#2b2b33" stroke-width=".8"/></svg>
    www.classroomaidecourse.com.au
  </div>
</section>

<!-- Page: units -->
<section class="page page--units">
  <aside class="sidebar">
    <div class="motto"><span class="motto__pill">STUDY</span><span class="motto__pill">BRIGHTFIELD</span><span class="motto__pill">ACHIEVE</span></div>
    <div class="sidebar__photo photo--class" role="img" aria-label="Photo of students studying at computers in a classroom"></div>
    <div class="options"><p class="options__title">Study Options</p>
      <p class="options__item">Correspondence</p><p class="options__item">Online</p><p class="options__item">Self Paced</p><p class="options__item">Blended</p></div>
  </aside>
  <div class="footer">
    <svg viewBox="0 0 384 78" preserveAspectRatio="none" aria-hidden="true">
      <path d="M0,14 C120,48 260,0 384,8 L384,78 L0,78 Z" fill="#81c9bd"/>
      <path d="M0,26 C120,62 260,12 384,22 L384,78 L0,78 Z" fill="#000080"/>
    </svg>
    <span class="footer__url">www.brightfieldtraining.com.au</span>
  </div>
  <div class="content">
    <h2 class="h">ABOUT CERTIFICATE III <small>(IN EDUCATION SUPPORT)</small></h2>
    <p class="p">This course is suitable if you are currently working as or seeking to work as a teacher aide in a primary, secondary or special needs school or community education setting. This Nationally Recognised course consists of 17 units:</p>
    <dl class="units">
      <dt>CHCECE006</dt><dd>Support behaviour of children and young people</dd>
      <dt>CHCEDS001</dt><dd>Comply with legislative, policy and industrial requirements in the education environment</dd>
      <dt>CHCEDS007</dt><dd>Work effectively with students and colleagues</dd>
      <dt>CHCEDS016</dt><dd>Support learning for students with disabilities in a classroom environment</dd>
      <dt>CHCEDS018</dt><dd>Support students with additional needs in the classroom environment</dd>
      <dt>CHCEDS002</dt><dd>Assist implementation of planned educational programs</dd>
      <dt>CHCEDS003</dt><dd>Contribute to student education in all developmental domains</dd>
      <dt>CHCDIV001</dt><dd>Work with diverse people</dd>
      <dt>CHCEDS008</dt><dd>Comply with school administrative requirements</dd>
      <dt>CHCEDS004</dt><dd>Contribute to organisation and management of classroom or centre</dd>
      <dt>CHCEDS005</dt><dd>Support the development of literacy and oral language skills</dd>
      <dt>CHCEDS006</dt><dd>Support the development of numeracy skills</dd>
      <dt>CHCEDS017</dt><dd>Contribute to the health and safety of students</dd>
      <dt>HLTWHS001</dt><dd>Participate in work health and safety</dd>
      <dt>CHCDIV002</dt><dd>Promote Aboriginal and/or Torres Strait Islander cultural safety</dd>
    </dl>
    <h2 class="h">ELECTIVE UNITS <small>(Choose 2 from the following)</small></h2>
    <dl class="units units--elective">
      <dt>CHCEDS024</dt><dd>Use educational strategies to support Aboriginal and/or Torres Strait Islander education</dd>
      <dt>CHCEDS032</dt><dd>Support learning and implementation of responsible behaviour</dd>
      <dt>CHCEDS012</dt><dd>Set up and sustain individual and small group learning areas</dd>
      <dt>CHCEDS011</dt><dd>Search and assess online information</dd>
      <dt>CHCDIS004</dt><dd>Communicate using augmentative and alternative communication strategies</dd>
      <dt>HLTAID003</dt><dd>Provide first aid*</dd>
    </dl>
    <p class="note-band">* Please read the first aid section in this document for further details on fees and conditions associated with selecting this unit as an elective.*</p>
    <h2 class="h">ENTRY REQUIREMENTS</h2>
    <p class="p">It is expected that students have well developed written and verbal communication skills, basic numeracy skills and basic computer operating skills. A working with children check (also known as a blue card in Qld) must be obtained prior to conducting your vocational placement. Refer back to our website for links to each State or Territory agency responsible for administering working with children checks.</p>
    <h2 class="h">DURATION</h2>
    <p class="p">You will have up to 2 years to complete but can progress at any pace. As a guide someone spending 8 hrs per week on assessment, could expect to complete the course in approximately 7 - 9 months. Please note that students receiving government funding / subsidies may be obligated to complete in a set time frame:</p>
    <p class="supplement"><b>Income Support Office</b> (education supplement):</p>
    <p class="supplement-rates"><span>• Full time - 40 weeks</span><span>• Part time - 69 weeks</span></p>
  </div>
</section>

<!-- Page: study mode -->
<section class="page page--study">
  <aside class="sidebar">
    <div class="motto"><span class="motto__pill">STUDY</span><span class="motto__pill">BRIGHTFIELD</span><span class="motto__pill">ACHIEVE</span></div>
    <div class="sidebar__photo photo--student" role="img" aria-label="Photo of a smiling student holding books"></div>
    <div class="options"><p class="options__title">Study Options</p>
      <p class="options__item">Correspondence</p><p class="options__item">Online</p><p class="options__item">Self Paced</p><p class="options__item">Blended</p></div>
  </aside>
  <div class="content">
    <h2 class="h">STUDY MODE</h2>
    <p class="p">Delivery and assessment of this course can be customised. Please discuss your options with Brightfield to ensure that we have created the course that best suits you.</p>
    <p class="p"><b>Self-paced</b> study means that you can study at times and locations that suit you. No assessment due dates and no timetabled lectures or webinars. You can choose to study online using an interactive student portal or via correspondence with all materials posted out to you. Fast track your study or take your time - the choice is yours.</p>
    <p class="p"><b>Blended</b> study has all the perks of self-paced study with the addition of face-to-face sessions with your trainer. You can book as many or as few face-to-face sessions as you like - the price in the table below is based on four face-to-face sessions.</p>
    <h2 class="h">ONLINE OR CORRESPONDENCE ?</h2>
    <p class="p">The course consists of two key components - Theory and Practical. For the theory component you may opt to receive course resources by correspondence or online.</p>
    <div class="sub"><span class="sub__mark"></span><p class="p"><b>Online :</b><br>benefit from an easy to navigate elearning course. The online course is interactive, meaning less readings and more visually engaging resources.</p></div>
    <div class="sub"><span class="sub__mark"></span><p class="p"><b>Correspondence :</b><br>receive course resources such as textbooks and assessments in a hardcopy format. Resources are presented in a student portfolio for easy management. Assessment is provided on a USB stick.</p></div>
    <h2 class="h">PRACTICAL</h2>
    <p class="p">Students not currently working in the education support industry will be required to complete 100 hours practical placement as part of their study. You may choose to do your placement as a full time block or part time (e.g. 2 days per week). The placement can be completed at any stage during your course. Brightfield will help you arrange your placement for you or you can arrange your own. Additional hours (up to 100hrs) of placement may be required for school based students, students on a traineeship, Early School leavers or those that have been assessed as having limited work/life experience. This will enable more time to develop skills in a work setting. In some instances the exact number of practical placement hours will need to be negotiated between the student, the trainer and the placement person.</p>
    <h2 class="h">ASSESSMENT</h2>
    <p class="p">Your assessment consists of two key areas:</p>
    <p class="p"><u>Theory assessment</u> that may include:<br>text activities, written questions, case studies, projects, evidence portfolios.</p>
    <p class="p"><u>Practical assessment</u> that includes demonstration of your skills in the workplace. Recorded as observations by your supervisor, practical placement person or trainer.</p>
    <h2 class="h">GOVERNMENT FUNDING</h2>
    <p class="p">This course is approved for funding through the following agencies/programs:</p>
    <ul class="list"><li>Certificate 3 Guarantee (eligible QLD residents only)</li><li>Commonwealth Traineeships (for new employees)</li><li>Income Support Office (Education Supplement)</li></ul>
    <p class="p">Contact us or complete our eligibility checklist and we will let you know if you or your employer may attract funding.</p>
    <span class="tag">Certificate 3 Guarantee</span>
    <p class="p">The Certificate 3 Guarantee aims to assist people gain their first post school Certificate III qualification regardless of their current employment status. To be eligible for this program you must:</p>
    <ul class="list"><li>Be aged 15 years or above and no longer be at school</li><li>Permanently reside in Queensland</li><li>Be an Australian citizen or New Zealand citizen or Australian permanent resident (including humanitarian entrants), or a temporary resident with the necessary visa and work permits on the pathway to permanent residency.</li><li>Not hold (or be currently enrolled in) a post school Certificate III or higher level qualification.</li></ul>
  </div>
  <div class="footer">
    <svg viewBox="0 0 381 78" preserveAspectRatio="none" aria-hidden="true">
      <path d="M0,14 C120,48 260,0 381,8 L381,78 L0,78 Z" fill="#81c9bd"/>
      <path d="M0,26 C120,62 260,12 381,22 L381,78 L0,78 Z" fill="#000080"/>
    </svg>
    <span class="footer__url">www.brightfieldtraining.com.au</span>
  </div>
</section>

<!-- Page: fees & enrolment -->
<section class="page page--fees">
  <aside class="sidebar">
    <div class="motto"><span class="motto__pill">STUDY</span><span class="motto__pill">BRIGHTFIELD</span><span class="motto__pill">ACHIEVE</span></div>
    <div class="sidebar__photo photo--learner" role="img" aria-label="Photo of a smiling student with glasses holding a notebook"></div>
    <div class="options"><p class="options__title">Study Options</p>
      <p class="options__item">Correspondence</p><p class="options__item">Online</p><p class="options__item">Self Paced</p><p class="options__item">Blended</p></div>
  </aside>
  <div class="content">
    <p class="p">Students approved for the Certificate 3 Guarantee program will pay a student contribution fee. Concession card holders, Aboriginal or Torres Strait Islander people and students who have graduated year 12 within the last 12 months will receive a concession rate.</p>
    <h2 class="h">PAYMENT</h2>
    <p class="p"><b>Note:</b> fees quoted below are inclusive of all mandatory course resources. Additional fees apply if you choose the unit HLTAID003 Apply first aid as an elective unit. Please read the first aid section in this document for further details.</p>
    <table class="fees">
      <tr><th>CHC30213 Certificate III in Education Support</th><th>Self-Paced</th></tr>
      <tr><td>Standard course fee including those receiving the Education Supplement (through Income Support Office), OR</td><td>$1,980</td></tr>
      <tr class="row--split"><td>For students who qualify for the Certificate 3 Guarantee:
        <ul class="list list--ticks"><li>Standard Student contribution fee</li><li>Student contribution fee - concessional students</li><li>Student contribution fee - Yr 12 fee free students</li></ul></td>
        <td><br>$500<br>$400<br>$0</td></tr>
    </table>
    <p class="p"><b>Note :</b> Add $800 to above prices if you would like the blended mode of training (includes 4 onsite sessions and is only available to those in SE QLD region).</p>
    <p class="p"><b>Payment plans</b> are offered at no additional cost! All Fees quoted above can be incorporated into a payment plan. You nominate the payment periods (i.e. weekly, fortnightly or monthly). You nominate the instalment amount you are comfortable paying each period (i.e. $50, $100, $200, etc.).</p>
    <h2 class="h">STUDENT SUPPORT</h2>
    <p class="p">Regardless of the study mode you select, you will have unlimited access to your trainer through phone, email and instant messaging. You may send your trainer drafts for feedback and comments. Each trainer has significant industry experience and will prove to be a valuable support network for you throughout the course.</p>
    <h2 class="h">HOW TO ENROL</h2>
    <p class="p">Read the Student Handbook and this Course Outline<br><b>You have 3 different ways to enrol :</b></p>
    <ol class="list list--num"><li>Go to brightfieldtraining.com.au/enrol-now to complete your enrolment online OR</li><li>Download an Enrolment Form from our website and return by email or post OR</li><li>Call us on 1300 555 019 to enrol over the phone</li></ol>
    <h2 class="h">COURSE COMMENCEMENT</h2>
    <p class="p">Upon receipt of your enrolment form a Brightfield Training staff member will contact you to conduct a pre-enrolment interview and to confirm your enrolment.</p>
    <h2 class="h">COURSE INDUCTION</h2>
    <p class="p">All Brightfield Training students will receive a course induction. Inductions may be completed face-to-face, on video call, or over the phone. During your induction, your trainer will: take time to explain how to navigate your course resources and assessments; and provide you with some guidance on the depth and content expected in some of the different assessments.</p>
    <h2 class="h">FIRST AID</h2>
    <p class="p">You have the option of selecting HLTAID003 Provide first aid as an elective unit within this course. Note: selecting this unit is not mandatory. Brightfield delivers this unit at select venues around Brisbane. Please contact us to find out upcoming course dates and venues. Alternatively, you are able to complete the first aid course with any provider in Australia. Some important points to consider if selecting HLTAID003 Provide first aid as an elective:</p>
    <ul class="list"><li>The cost of the first aid unit is not included in Brightfield Training's course fee. You will need to pay the listed course fee to your selected first aid provider.</li><li>Ensure that you are booking into a first aid course that includes the nationally recognised unit HLTAID003 Provide First Aid.</li></ul>
    <h2 class="h">COURSE COMPLETION</h2>
    <p class="p">On successful completion of all course requirements you will be issued a Nationally Recognised Certificate III in Education Support. All students completing or discontinuing their studies will be required to complete a student survey.</p>
  </div>
  <div class="footer">
    <svg viewBox="0 0 384 78" preserveAspectRatio="none" aria-hidden="true">
      <path d="M0,14 C120,48 260,0 384,8 L384,78 L0,78 Z" fill="#81c9bd"/>
      <path d="M0,26 C120,62 260,12 384,22 L384,78 L0,78 Z" fill="#000080"/>
    </svg>
    <span class="footer__url">www.brightfieldtraining.com.au</span>
  </div>
</section>

</body>
</html>
```